Tova Brisk Fitness Coaching Project

I am a personal trainer based in London. My services include one-on-one PT sessions, bootcamps.
I would like the design to be minimalistic. With light colours: white, pink, purple.
I specialise in weight loss, flexibility, mobility.

Tova Penrick
Personal Trainer
Email: tova.penrick@mailgrove.net
tel: 07500 918 243
Instagram: Tova Brisk

Target Market(s)

adults, mostly females (age 18-50).

Industry/Entity Type

Fitness

Contact Information for Business Card

Tova Penrick
Personal Trainer
tel: 07500 918 243
Instagram: Tova Brisk

Font styles to use
Serif

Colors
eea4c8
fbd4d5
fdf9cf
cfeae6
cee9f5

Requirements
Nice to have
• minimalistic style
• easy to read and remember

```html
<!DOCTYPE html>
<html lang="en">
<head>
<meta charset="utf-8">
<title>Tova Penrick – Personal Trainer Business Card</title>
<link rel="stylesheet" href="https://fonts.googleapis.com/css2?family=Montserrat:wght@400;700;800&family=Open+Sans:wght@400;600&display=swap">
<style>
  :root {
    --backdrop: #ececec;
    --card-white: #ffffff;
    --ink: #3b3b3b;
    --ink-soft: #4a4a4a;
    --pink: #e46aa8;
    --pink-light: #eea4c8;
    --lavender: #c9b6e0;
    --sky: #cee9f5;
    --photo-warm: #b58a78;
    --photo-deep: #6b4a3c;
    --photo-light: #f3e6df;
  }
  * { box-sizing: border-box; margin: 0; padding: 0; }
  html, body { width: 1200px; height: 738px; overflow: hidden; }
  body {
    background: var(--backdrop);
    font-family: "Open Sans", Arial, sans-serif;
    position: relative;
  }
  .card {
    position: absolute;
    top: 226px;
    width: 500px;
    height: 286px;
    overflow: hidden;
    box-shadow: 0 10px 28px rgba(0,0,0,0.12);
  }

  /* Front card */
  .card--front {
    left: 70px;
    background: linear-gradient(100deg, var(--pink) 0%, #e98dbd 40%, var(--lavender) 75%, var(--sky) 100%);
  }
  .card--front .portrait {
    position: absolute;
    right: 0; top: 0;
    width: 62%; height: 100%;
    background:
      linear-gradient(90deg, rgba(233,141,189,1) 0%, rgba(233,141,189,0) 35%),
      radial-gradient(ellipse at 55% 45%, rgba(243,230,223,0.75) 0%, rgba(181,138,120,0.55) 35%, rgba(201,182,224,0.4) 70%, rgba(206,233,245,0.5) 100%);
  }
  .card--front .name {
    position: absolute;
    left: 46px; top: 134px;
    font-family: "Montserrat", Arial, sans-serif;
    font-weight: 800;
    font-size: 38px;
    letter-spacing: 0.5px;
    color: rgba(255,255,255,0.85);
  }
  .card--front .role {
    position: absolute;
    left: 46px; top: 196px;
    font-family: "Montserrat", Arial, sans-serif;
    font-weight: 400;
    font-size: 18px;
    letter-spacing: 1px;
    color: rgba(255,255,255,0.75);
  }
  .card--front .role::before {
    content: "•";
    margin-right: 14px;
  }

  /* Back card */
  .card--back {
    left: 630px;
    background: var(--card-white);
  }
  .card--back .portrait {
    position: absolute;
    right: 0; top: 0;
    width: 46%; height: 100%;
    background:
      linear-gradient(90deg, rgba(255,255,255,1) 0%, rgba(255,255,255,0) 38%),
      linear-gradient(0deg, rgba(255,255,255,0.9) 0%, rgba(255,255,255,0) 22%),
      radial-gradient(ellipse at 62% 42%, var(--photo-light) 0%, var(--photo-warm) 32%, var(--photo-deep) 62%, #e9e2dc 100%);
  }
  .contact {
    position: absolute;
    left: 40px; top: 92px;
    color: var(--ink);
  }
  .contact .name {
    font-family: "Montserrat", Arial, sans-serif;
    font-weight: 700;
    font-size: 28px;
    letter-spacing: 0.3px;
  }
  .contact .role {
    margin-top: 12px;
    font-size: 11.5px;
    letter-spacing: 0.4px;
    color: var(--ink-soft);
  }
  .contact-list {
    list-style: none;
    margin-top: 12px;
  }
  .contact-list li {
    display: flex;
    align-items: center;
    gap: 14px;
    font-size: 14.5px;
    color: var(--ink-soft);
    height: 24px;
  }
  .contact-list .icon {
    width: 14px; height: 14px;
    flex: none;
    fill: var(--ink);
  }
  .contact-list .dot {
    width: 10px; height: 10px;
    margin: 0 2px;
    border-radius: 50%;
    background: var(--ink);
    flex: none;
  }
</style>
</head>
<body>
  <section class="card card--front" aria-label="Business card front">
    <div class="portrait" role="img" aria-label="Soft-focus portrait photo of the trainer with curly hair, smiling"></div>
    <h1 class="name">TOVA PENRICK</h1>
    <p class="role">PERSONAL TRAINER</p>
  </section>

  <section class="card card--back" aria-label="Business card back">
    <div class="portrait" role="img" aria-label="Portrait photo of the trainer with long curly hair, smiling"></div>
    <div class="contact">
      <h2 class="name">TOVA PENRICK</h2>
      <p class="role">PERSONAL TRAINER</p>
      <ul class="contact-list">
        <li>
          <svg class="icon" viewBox="0 0 16 16" aria-hidden="true">
            <path d="M2 5c0-2 2-3 6-3s6 1 6 3v1h-3V5H5v1H2z"/>
            <rect x="3" y="7" width="10" height="7" rx="1"/>
          </svg>
          07500 918 243
        </li>
        <li>
          <svg class="icon" viewBox="0 0 16 16" aria-hidden="true">
            <rect x="1" y="3" width="14" height="10" rx="1"/>
            <path d="M1.5 3.5 8 9l6.5-5.5" fill="none" stroke="#fff" stroke-width="1.4"/>
          </svg>
          tova.penrick@mailgrove.net
        </li>
        <li>
          <span class="dot" aria-hidden="true"></span>
          Tova Brisk
        </li>
      </ul>
    </div>
  </section>
</body>
</html>
```